Astrologer needs a design for business card

I need a business card design for my job in astrology and flower therapy.
In front side need the information add file.

In back side need the informations above:
INTERPRETAÇÕES
TENDÊNCIAS
AUTOCONHECIMENTO
ANÁLISE VOCACIONAL
DIRECIONAMENTO DE CARREIRA
RELACIONAMENTOS
ASTROLOGIA EMPRESARIAL
TERAPIA FLORAL – Florias de Munter e Caio Brenvide

OLVE

```html
<!DOCTYPE html>
<html lang="pt">
<head>
<meta charset="utf-8">
<title>Marevna Solt – Cartão de Visita</title>
<link rel="stylesheet" href="https://fonts.googleapis.com/css2?family=Arimo:wght@400;700&family=Cormorant+Garamond:wght@500;600&display=swap">
<style>
  :root {
    --backdrop: #e9e8ec;
    --card-dark: #3b3a3d;
    --card-light: #f1f1f3;
    --ink-white: #f4f4f4;
    --ink-dark: #3a3a3c;
    --gold-light: #e6c979;
    --gold-mid: #b8913f;
    --gold-deep: #7d5e22;
    --rule: #8a8a8c;
  }
  * { margin: 0; padding: 0; box-sizing: border-box; }
  html, body { width: 1200px; height: 900px; overflow: hidden; }
  body {
    background: var(--backdrop);
    display: flex;
    align-items: center;
    justify-content: center;
    gap: 40px;
  }
  .card {
    width: 540px;
    height: 350px;
    box-shadow: 0 6px 18px rgba(0,0,0,0.28);
    position: relative;
    overflow: hidden;
  }
  .card-back {
    background: linear-gradient(160deg, #444346, var(--card-dark) 60%, #343336);
  }
  .zodiac-art { width: 100%; height: 100%; }

  .card-front {
    display: flex;
    background: var(--card-dark);
  }
  .identity {
    width: 313px;
    flex: none;
    padding: 80px 8px 0 16px;
    color: var(--ink-white);
  }
  .name-first {
    font-family: "Arimo", Arial, sans-serif;
    font-weight: 700;
    font-size: 62px;
    line-height: 0.95;
    letter-spacing: -1.5px;
    text-align: right;
  }
  .name-row {
    display: flex;
    align-items: flex-end;
    justify-content: flex-end;
    gap: 5px;
  }
  .name-last {
    font-family: "Arimo", Arial, sans-serif;
    font-weight: 700;
    font-size: 36px;
    line-height: 1;
    background: linear-gradient(180deg, var(--gold-light), var(--gold-mid) 55%, var(--gold-deep));
    -webkit-background-clip: text;
    background-clip: text;
    color: transparent;
  }
  .specialties {
    font-family: "Cormorant Garamond", Georgia, serif;
    font-weight: 600;
    font-size: 11.5px;
    line-height: 1.05;
    color: var(--gold-light);
    text-transform: uppercase;
    padding-bottom: 3px;
    white-space: nowrap;
  }
  .services {
    display: flex;
    align-items: flex-start;
    justify-content: flex-end;
    margin-top: 12px;
    font-family: "Cormorant Garamond", Georgia, serif;
    font-weight: 500;
    color: var(--ink-white);
    text-transform: uppercase;
    white-space: nowrap;
  }
  .service-col {
    padding: 0 5px;
    border-left: 1px solid var(--rule);
  }
  .service-col:first-child { border-left: none; padding-left: 0; }
  .service-col:last-child { padding-right: 0; }
  .service-title { font-size: 10px; letter-spacing: 0.2px; line-height: 1.2; }
  .service-item { font-size: 7px; line-height: 1.3; }
  .service-item.wide { width: 0; }
  .service-item .note { text-transform: none; font-size: 6.5px; }
  .contact {
    flex: 1;
    background: var(--card-light);
    padding: 148px 0 0 16px;
    font-family: "Arimo", Arial, sans-serif;
    color: var(--ink-dark);
  }
  .contact-line {
    display: flex;
    align-items: center;
    gap: 8px;
    white-space: nowrap;
  }
  .contact-phone { font-size: 19px; }
  .contact-email { font-size: 13px; margin-top: 10px; }
  .contact-icon { flex: none; }
</style>
</head>
<body>
  <section class="card card-back" aria-label="Verso do cartão">
    <svg class="zodiac-art" viewBox="0 0 540 350" role="img" aria-label="Doze figuras dos signos do zodíaco em branco sobre fundo cinza-escuro">
      <rect width="540" height="350" fill="none"/>
    </svg>
  </section>

  <section class="card card-front" aria-label="Frente do cartão">
    <div class="identity">
      <h1 class="name-first">Marevna</h1>
      <div class="name-row">
        <span class="name-last">Solt</span>
        <p class="specialties">Mapas Astrológicos<br>Terapia Floral</p>
      </div>
      <div class="services">
        <div class="service-col">
          <p class="service-title">Interpretações</p>
          <p class="service-item">Análise Vocacional</p>
          <p class="service-item wide">Terapia Floral – <span class="note">Florias de Munter e Caio Brenvide</span></p>
        </div>
        <div class="service-col">
          <p class="service-title">Tendências</p>
          <p class="service-item">Relacionamentos</p>
        </div>
        <div class="service-col">
          <p class="service-title">Autoconhecimento</p>
          <p class="service-item">Direcionamento de Carreira</p>
          <p class="service-item">Astrologia Empresarial</p>
        </div>
      </div>
    </div>
    <div class="contact">
      <p class="contact-line contact-phone">
        <svg class="contact-icon" width="16" height="26" viewBox="0 0 16 26" aria-hidden="true">
          <rect x="1" y="1" width="14" height="24" rx="2.5" fill="none" stroke="#3a3a3c" stroke-width="2"/>
          <rect x="3.5" y="4.5" width="9" height="14" fill="#3a3a3c"/>
          <circle cx="8" cy="21.5" r="1.3" fill="#3a3a3c"/>
        </svg>
        (51) 9000-2746
      </p>
      <p class="contact-line contact-email">
        <svg class="contact-icon" width="16" height="11" viewBox="0 0 16 11" aria-hidden="true">
          <rect width="16" height="11" fill="#3a3a3c"/>
          <path d="M0 0 L8 6 L16 0" fill="none" stroke="#f1f1f3" stroke-width="1.3"/>
        </svg>
        marevnasolt@correio.com
      </p>
    </div>
  </section>
</body>
</html>
```